Business software developers new website

We need to redesign our website. Our current website is http://www.plumvista.net/index.html, which is outdated and needs a new look. We moved out from web design and have concentrated more on the back end of the systems, for example, system support and security and cloud-based applications. Our major clients include both private and government sectors. We would like to see some designs that are all in one page, simple and clean. Prefer illustrator or obstructed images instead of real-life photos. Must look futuristic yet friendly. Attached the new logo for your references and good luck.

Target Market(s)

Medium to big company for their IT or data management. Either improve or upgrade their current system.

Industry/Entity Type

Business Software

Number of Pages Required

1 page

Colors

Designer to choose colors to be used in the design.

Requirements
Must have
• Simple and clean. Individual assets must be provided in the correct size and format(png or jpeg). Prefer Goggle fonts. Even though the logo color is red, grey and black, still prefer some modern colors that go well with red. When design, must consider the possibility to convert it into responsive.
Nice to have
• White background
Should not have
• real life photos, no slider

```html
<!DOCTYPE html>
<html lang="en">
<head>
<meta charset="utf-8">
<title>Plumvista.net — System Support and Security</title>
<link href="https://fonts.googleapis.com/css2?family=Poppins:wght@400;500;600;700&family=Roboto:wght@400;500&display=swap" rel="stylesheet">
<style>
:root{
  --red:#e2223b;
  --red-soft:#f1b9c2;
  --magenta:#dc2670;
  --purple:#8b3b9b;
  --navy:#241a8a;
  --blue:#3a4fd0;
  --ink:#1f1f24;
  --text:#555a63;
  --panel:#f3f3f8;
  --white:#ffffff;
}
*{margin:0;padding:0;box-sizing:border-box}
html,body{width:1200px;height:4267px;overflow:hidden}
body{position:relative;background:var(--white);font-family:"Roboto",Arial,sans-serif;color:var(--text)}
.abs{position:absolute}
h1,h2,h3,.logo,.nav a,.phone-pill,.btn-send{font-family:"Poppins",Arial,sans-serif}
h2.section-title{font-size:42px;font-weight:600;color:var(--ink);text-align:center;letter-spacing:-.3px}
.lead{font-size:13.5px;line-height:22px;text-align:center;color:#3b3f46}
.body-copy{font-size:12px;line-height:21.8px;color:#555a63}

/* hero */
.hero-bg{left:0;top:0;width:1200px;height:650px}
.logo{left:94px;top:40px;font-size:34px;font-weight:500;color:var(--white);letter-spacing:-.5px}
.nav{left:583px;top:52px;display:flex;gap:0}
.nav a{position:absolute;font-size:12px;font-weight:600;color:var(--white);text-decoration:none;white-space:nowrap}
.phone-pill{left:961px;top:41px;width:145px;height:38px;border-radius:19px;background:var(--white);color:var(--red);font-size:13px;font-weight:600;display:flex;align-items:center;justify-content:center;gap:6px}
.hero-title{left:94px;top:205px;font-size:56px;line-height:70px;font-weight:700;color:var(--white)}
.hero-sub{left:94px;top:344px;font-size:20px;font-weight:400;color:var(--white);font-family:"Poppins",Arial,sans-serif;letter-spacing:.3px}
.hero-arrows{left:93px;top:456px;display:flex;gap:8px}
.arrow-btn{width:36px;height:36px;border-radius:50%;border:2px solid var(--white);display:flex;align-items:center;justify-content:center}
.arrow-btn.active{background:var(--white)}
.hero-art{left:530px;top:100px;width:580px;height:510px;border-radius:46% 40% 30% 44%;background:linear-gradient(150deg,#c9d6ff 0%,#8d6cf0 45%,#f2c94c 100%);opacity:.85}

/* about */
.about-title{left:0;top:684px;width:1200px}
.about-lead{left:260px;top:742px;width:680px}
.about-copy{left:94px;top:882px;width:560px}
.about-art{left:703px;top:790px;width:395px;height:345px}

/* services */
.services-panel{left:0;top:1150px;width:1200px;height:720px}
.services-title{left:0;top:1255px;width:1200px}
.services-lead{left:270px;top:1318px;width:660px}
.service{width:260px;text-align:center}
.service h3{font-size:15px;font-weight:600;color:var(--ink);margin-top:14px}
.service p{font-size:11.5px;line-height:17px;color:#666b73;margin-top:10px}
.service ul{list-style:none;margin-top:12px;font-size:11.5px;line-height:22px;color:#666b73}
.plus-btn{width:26px;height:26px;border-radius:50%;background:var(--red);color:var(--white);font-size:16px;line-height:26px;text-align:center;margin:10px auto 0;box-shadow:0 3px 8px rgba(226,34,59,.35)}
.dash{height:0;border-top:2px dashed #cfd0d8;width:140px}

/* clients */
.clients-art{left:0;top:1855px;width:510px;height:360px}
.clients-title{left:566px;top:1884px;font-size:42px;font-weight:600;color:var(--ink)}
.clients-lead{left:566px;top:1944px;width:440px;font-size:12.5px;line-height:22px;color:#33373d}
.clients-copy{left:566px;top:2004px;width:540px}
.project{width:313px}
.project .shot{height:194px;border-radius:4px;box-shadow:0 6px 18px rgba(0,0,0,.12)}
.project h3{font-size:15px;font-weight:600;color:var(--ink);margin-top:24px}
.project p{font-size:11.5px;line-height:21.5px;color:#5a5f67;margin-top:10px}
.project a{display:block;font-size:11.5px;color:var(--red);text-decoration:none;margin-top:6px}

/* testimonial */
.says-title{left:0;top:2752px;width:1200px}
.says-sub{left:0;top:2808px;width:1200px;font-size:13px;text-align:center;color:#444}
.quote-card{left:222px;top:2883px;width:756px;height:237px;background:var(--panel)}
.quote-person{left:248px;top:2830px;width:207px;height:290px;border-radius:100px 100px 0 0;background:linear-gradient(180deg,#e9d5c4 0%,#3a3f5c 55%,#232742 100%)}
.quote-text{left:497px;top:2960px;width:445px;font-size:12px;line-height:21.5px;color:#555}
.quote-name{left:497px;top:3064px;font-size:12.5px;font-weight:500;color:var(--red)}

/* faq */
.faq-title{left:94px;top:3305px;font-size:40px;font-weight:600;color:var(--ink)}
.faq-q{left:94px;width:436px;height:40px}
.faq-q span{position:absolute;left:12px;top:11px;font-size:12.5px;color:var(--white)}
.faq-a{left:106px;top:3428px;width:420px;font-size:11.5px;line-height:21.5px;color:#5a5f67}
.faq-art{left:695px;top:3244px;width:505px;height:360px}

/* footer */
.footer-bg{left:0;top:3600px;width:1200px;height:667px}
.contact-card{left:156px;top:3687px;width:887px;height:265px;background:var(--white);border-radius:8px;box-shadow:0 10px 30px rgba(60,20,80,.12)}
.contact-card h2{position:absolute;left:48px;top:104px;font-size:24px;font-weight:500;color:var(--ink)}
.field{position:absolute;border:1px solid #cfd0d6;border-radius:2px;font-size:11px;color:#777;padding:8px 10px}
.btn-send{position:absolute;left:726px;top:196px;width:108px;height:38px;border-radius:19px;background:var(--red);color:var(--white);font-size:13px;font-weight:600;display:flex;align-items:center;justify-content:center;box-shadow:0 4px 10px rgba(226,34,59,.35)}
.f-head{font-family:"Poppins",Arial,sans-serif;font-size:14px;font-weight:600;color:var(--white)}
.f-text{font-size:11px;line-height:18.5px;color:rgba(255,255,255,.92)}
.f-links{list-style:none;font-size:11px;color:var(--white);line-height:29px}
.social{display:flex;gap:9px}
.social i{width:22px;height:22px;border-radius:50%;background:var(--white);display:block}
.affiliate{left:940px;top:4063px;display:flex;align-items:center;gap:8px;font-family:"Poppins",Arial,sans-serif;font-size:22px;font-weight:600;color:var(--white)}
.affiliate b{width:16px;height:16px;background:var(--white);display:block}
.copyright{right:94px;top:4165px;font-size:10.5px;color:rgba(255,255,255,.9)}
</style>
</head>
<body>

<!-- HERO -->
<svg class="abs hero-bg" viewBox="0 0 1200 650" aria-hidden="true">
  <defs>
    <linearGradient id="heroGrad" x1="0" y1="0" x2="1" y2="0.3">
      <stop offset="0" stop-color="#8a3c98"/>
      <stop offset="0.55" stop-color="#b92e86"/>
      <stop offset="1" stop-color="#e2276b"/>
    </linearGradient>
  </defs>
  <path d="M0 0 H1200 V648 L90 555 Q0 548 0 470 Z" fill="url(#heroGrad)"/>
</svg>
<div class="abs logo">plumvista.net</div>
<nav class="abs nav">
  <a style="left:0">Home</a>
  <a style="left:74px">Our Services</a>
  <a style="left:183px">Our Clients</a>
  <a style="left:286px">Contact</a>
</nav>
<div class="abs phone-pill">
  <svg width="12" height="12" viewBox="0 0 24 24"><path d="M6.6 10.8a15.1 15.1 0 0 0 6.6 6.6l2.2-2.2c.3-.3.7-.4 1-.2 1.1.4 2.3.6 3.6.6.6 0 1 .4 1 1V20c0 .6-.4 1-1 1C10.6 21 3 13.4 3 4c0-.6.4-1 1-1h3.5c.6 0 1 .4 1 1 0 1.3.2 2.5.6 3.6.1.3 0 .7-.2 1z" fill="var(--red)"/></svg>
  617 3820 4416
</div>
<h1 class="abs hero-title">System Support<br>and Security</h1>
<div class="abs hero-sub">and cloud-based Applications</div>
<div class="abs hero-arrows">
  <div class="arrow-btn"><svg width="16" height="16" viewBox="0 0 24 24"><path d="M19 12H5m6-6-6 6 6 6" stroke="#fff" stroke-width="2" fill="none"/></svg></div>
  <div class="arrow-btn active"><svg width="16" height="16" viewBox="0 0 24 24"><path d="M5 12h14m-6-6 6 6-6 6" stroke="var(--red)" stroke-width="2" fill="none"/></svg></div>
</div>
<div class="abs hero-art" role="img" aria-label="Illustration of people working with a large server tower and stacked server units"></div>

<!-- decorative rings -->
<svg class="abs" style="left:0;top:570px" width="160" height="280" aria-hidden="true"><circle cx="20" cy="140" r="100" fill="none" stroke="#fbe6ea" stroke-width="44"/></svg>

<!-- ABOUT -->
<h2 class="abs section-title about-title">About Us</h2>
<p class="abs lead about-lead">Plumvista.net is an Australian based Software and Web Development Company that provides individual technology solutions and professional software for clients worldwide.</p>
<p class="abs body-copy about-copy">Plumvista.net is an Australian based Software and Web Development Company that provides individual technology solutions and professional software for clients worldwide.Our work is based on quality sales, customer and technical support services.Being oriented towards innovative productivity in our work, we come up with essential tools for online business enhancing. Our programming specialists focus on delivering solutions for small start-ups as well as large organizations and companies. The team of purposeful and experienced professionals works hard to extract maximum performance from modern information technologies. Providing the best quality of service and excellence of support we established a global presence in the software market. Our clients come from all over the world. Click here for more information on the services we provide.</p>
<svg class="abs about-art" viewBox="0 0 395 345" role="img" aria-label="Illustration of a cloud server in a dark blue blob">
  <defs><linearGradient id="aboutGrad" x1="0" y1="0" x2="1" y2="1"><stop offset="0" stop-color="#3b2fc4"/><stop offset="1" stop-color="#1d1675"/></linearGradient></defs>
  <path d="M60 60 Q170 -10 300 30 Q410 70 385 200 Q360 330 220 340 Q60 350 15 230 Q-20 120 60 60Z" fill="#b7e3ee"/>
  <path d="M50 70 Q160 10 290 45 Q395 80 370 205 Q345 325 210 335 Q65 340 25 235 Q-5 135 50 70Z" fill="url(#aboutGrad)"/>
</svg>

<!-- SERVICES -->
<svg class="abs services-panel" viewBox="0 0 1200 720" aria-hidden="true">
  <defs><linearGradient id="panelGrad" x1="0" y1="0" x2="0" y2="1"><stop offset="0" stop-color="#f3f3f8"/><stop offset="0.8" stop-color="#f6f6fa"/><stop offset="1" stop-color="#ffffff"/></linearGradient></defs>
  <path d="M0 110 Q0 80 40 78 L1120 40 Q1200 36 1200 110 V720 H0Z" fill="url(#panelGrad)"/>
</svg>
<h2 class="abs section-title services-title">Our Services</h2>
<p class="abs lead services-lead">Plumvista.net is an Australian based Software and Web Development Company that provides individual technology solutions and professional software for clients worldwide.</p>

<svg class="abs" style="left:0;top:1385px" width="1200" height="205" aria-hidden="true">
  <defs><linearGradient id="blobGrad" x1="0" y1="0" x2="1" y2="1"><stop offset="0" stop-color="#e8452c"/><stop offset="1" stop-color="#d81b3f"/></linearGradient></defs>
  <g id="blobSet">
    <g transform="translate(95,0)">
      <path d="M20 30 Q60 -10 140 10 Q225 35 222 105 Q215 175 120 190 Q25 205 5 125 Q-5 65 20 30Z" fill="#f2c4cb"/>
      <path d="M10 30 Q50 -8 130 8 Q215 30 210 100 Q205 170 110 188 Q15 205 0 120 Q-10 65 10 30Z" fill="url(#blobGrad)"/>
      <g stroke="#fff" stroke-width="2.5" fill="none"><rect x="70" y="70" width="58" height="42" rx="3"/><path d="M88 124h24M100 112v12"/><rect x="118" y="84" width="26" height="40" rx="3"/><path d="M80 83l6 5-6 5M92 96h14"/></g>
    </g>
    <g transform="translate(487,0)">
      <path d="M20 30 Q60 -10 140 10 Q225 35 222 105 Q215 175 120 190 Q25 205 5 125 Q-5 65 20 30Z" fill="#f2c4cb"/>
      <path d="M10 30 Q50 -8 130 8 Q215 30 210 100 Q205 170 110 188 Q15 205 0 120 Q-10 65 10 30Z" fill="url(#blobGrad)"/>
      <g stroke="#fff" stroke-width="2.5" fill="none"><path d="M109 62l26 10v22c0 18-12 28-26 34-14-6-26-16-26-34V72z"/><rect x="99" y="90" width="20" height="16" rx="2"/><path d="M103 90v-6a6 6 0 0 1 12 0v6"/></g>
    </g>
    <g transform="translate(878,0)">
      <path d="M20 30 Q60 -10 140 10 Q225 35 222 105 Q215 175 120 190 Q25 205 5 125 Q-5 65 20 30Z" fill="#f2c4cb"/>
      <path d="M10 30 Q50 -8 130 8 Q215 30 210 100 Q205 170 110 188 Q15 205 0 120 Q-10 65 10 30Z" fill="url(#blobGrad)"/>
      <g stroke="#fff" stroke-width="2.5" fill="none"><circle cx="108" cy="82" r="22"/><path d="M100 104v14h16v-14M102 122h12M86 104v22m-5-5 5 5 5-5M130 126v-22m-5 5 5-5 5 5"/></g>
    </g>
  </g>
</svg>
<div class="abs dash" style="left:334px;top:1486px"></div>
<div class="abs dash" style="left:728px;top:1486px"></div>

<div class="abs service" style="left:73px;top:1592px">
  <h3>Programming</h3>
  <p>We specialize in a variety of programming languages</p>
  <ul><li>Python</li><li>PostgreSQL</li><li>PHP</li></ul>
  <div class="plus-btn">+</div>
</div>
<div class="abs service" style="left:466px;top:1592px">
  <h3>W3C Compliant</h3>
  <p>All of our sites are W3C compliant, so you never have to worry about incompatibilities between browsers.</p>
</div>
<div class="abs service" style="left:856px;top:1592px">
  <h3>Hosting Solution</h3>
  <p>We offer competitive hosting solutions with all of our projects so you never have to worry about finding your site the right home.</p>
</div>

<!-- CLIENTS -->
<svg class="abs clients-art" viewBox="0 0 510 360" role="img" aria-label="Illustration of two business people shaking hands over a contract">
  <defs><linearGradient id="clientGrad" x1="0" y1="0" x2="1" y2="0.6"><stop offset="0" stop-color="#1f178a"/><stop offset="1" stop-color="#4a6fe0"/></linearGradient></defs>
  <path d="M0 90 Q140 5 340 25 Q505 45 505 140 Q500 260 360 330 Q250 375 160 330 Q90 295 0 310Z" fill="url(#clientGrad)"/>
</svg>
<h2 class="abs clients-title">Our Clients</h2>
<p class="abs clients-lead">Creativity, engineering and experienced management help us to provide our clients with innovative,&nbsp; high-grade software and web design solutions,</p>
<p class="abs body-copy clients-copy">Which save them time and money, automate and bring robust functionality and performance into their businesses. Plumvista.net undertakes many small projects, for example:Human Resource Management System, Warehouse Inventory Management System, including business to business communications with the CRO, Data Entry Streamlining and Content Management Systems.<br>We are also extremely experienced in the long term support of comprehensive web based business systems providing ongoing development, maintenance, data entry services and enhancements to these systems. One of our long term clients, ACRS (Australian Company Registration Services), have been using our services since 2001.</p>

<div class="abs project" style="left:94px;top:2272px">
  <div class="shot" role="img" aria-label="Screenshot of the Brightcoin currency matching website" style="background:linear-gradient(180deg,#7d7f86 0%,#c9cbd0 22%,#f5f5f5 30%,#f2f2f2 100%)"></div>
  <h3>Brightcoin</h3>
  <p>International currency matching system that allows expat Australians to transfer money between countries without the excessive bank fees.</p>
  <a>http://www.brightcoin.com</a>
</div>
<div class="abs project" style="left:443px;top:2272px">
  <div class="shot" role="img" aria-label="Screenshot of the Cell Therapy Society of Oceania website with a city skyline" style="background:linear-gradient(180deg,#f4f4f6 0%,#f4f4f6 22%,#6d8fc4 34%,#3c5f96 70%,#283a5a 100%)"></div>
  <h3>CTSO</h3>
  <p>The Cell Therapy Society of Oceania held its inaugural Annual Scientific Meeting in Canberra in 2000, and it has developed to include Tissue &amp; Cellular...</p>
  <a>http://www.ctso.org.au</a>
</div>
<div class="abs project" style="left:793px;top:2272px">
  <div class="shot" role="img" aria-label="Screenshot of the Marcellos restaurant website" style="background:linear-gradient(180deg,#2a2522 0%,#3b2f28 35%,#8a6446 60%,#2a2522 100%)"></div>
  <h3>Marcellos</h3>
  <p>Tom Verano has been welcoming friends to Marcellos for over 35 years. Generation after generation of tourists and locals alike have been experiencing the ...</p>
  <a>http://www.marcellos.com.au</a>
</div>

<!-- TESTIMONIAL -->
<svg class="abs" style="left:960px;top:2610px" width="240" height="440" aria-hidden="true"><circle cx="210" cy="220" r="150" fill="none" stroke="#fbe6ea" stroke-width="70"/></svg>
<h2 class="abs section-title says-title">Our Client Says</h2>
<p class="abs says-sub">We are loving your tesimonials and we balue your reviews</p>
<div class="abs quote-card"></div>
<div class="abs quote-person" role="img" aria-label="Illustration of a smiling businessman in a dark suit"></div>
<svg class="abs" style="left:176px;top:3080px" width="82" height="82" aria-hidden="true"><path d="M70 30 A33 33 0 1 0 72 52" fill="none" stroke="var(--red)" stroke-width="12"/></svg>
<svg class="abs" style="left:497px;top:2928px" width="46" height="34" aria-hidden="true"><path d="M2 34V18Q2 2 18 0v7q-7 2-7 9h7v18zM26 34V18Q26 2 42 0v7q-7 2-7 9h7v18z" fill="var(--red)"/></svg>
<p class="abs quote-text">Plumvista.net got us top rankings on all of the major search engines where in the past we were unable to even show up on them.Plumvista.net did what they promised, when they promised, all at a fair price.<br><span style="display:block;margin-top:8px">I'm very happy with my site!</span></p>
<div class="abs quote-name">Rowan Pell</div>

<!-- FAQ -->
<h2 class="abs faq-title">FAQ’s</h2>
<svg class="abs faq-q" style="top:3367px" viewBox="0 0 436 40" aria-hidden="true"><path d="M0 0H416L436 40H0Z" fill="var(--red)"/><path d="M400 18l4 4 4-4" stroke="#fff" stroke-width="1.5" fill="none"/></svg>
<div class="abs faq-q" style="top:3367px"><span>Q. How much does a web site powered by Plumvista.net cost?</span></div>
<p class="abs faq-a"><span style="color:var(--red)">A.</span> The Cell Therapy Society of Oceania held its inaugural Annual Scientific Meeting in Carbe</p>
<svg class="abs faq-q" style="top:3492px" viewBox="0 0 436 40" aria-hidden="true"><path d="M0 0H416L436 40H0Z" fill="var(--red)"/><path d="M402 16l4 4-4 4" stroke="#fff" stroke-width="1.5" fill="none"/></svg>
<div class="abs faq-q" style="top:3492px"><span>Q. How long does it take to have a web site designed?</span></div>
<svg class="abs faq-art" viewBox="0 0 505 360" role="img" aria-label="Illustration of a support agent with a headset holding a FAQ sign">
  <defs><linearGradient id="faqGrad" x1="0" y1="0" x2="1" y2="1"><stop offset="0" stop-color="#2a1e9a"/><stop offset="1" stop-color="#3f5fd8"/></linearGradient></defs>
  <path d="M20 90 Q40 20 170 12 Q330 0 505 40 V300 Q330 340 170 300 Q0 260 20 90Z" fill="url(#faqGrad)"/>
  <rect x="12" y="215" width="390" height="135" fill="#eeeef0"/>
</svg>

<!-- FOOTER -->
<svg class="abs footer-bg" viewBox="0 0 1200 667" aria-hidden="true">
  <defs><linearGradient id="footGrad" x1="0" y1="0" x2="1" y2="0"><stop offset="0" stop-color="#9a3a92"/><stop offset="0.5" stop-color="#c42c80"/><stop offset="1" stop-color="#dd2a6c"/></linearGradient></defs>
  <path d="M0 98 Q420 130 720 150 Q1020 170 1100 130 Q1200 80 1200 190 V667 H0Z" fill="url(#footGrad)"/>
  <path d="M0 400 Q60 300 220 250" stroke="rgba(255,255,255,.15)" fill="none"/>
  <path d="M0 420 Q70 320 240 262" stroke="rgba(255,255,255,.15)" fill="none"/>
</svg>
<form class="abs contact-card">
  <h2>Quick Contact</h2>
  <div class="field" style="left:256px;top:48px;width:286px;height:39px">Name</div>
  <div class="field" style="left:549px;top:48px;width:286px;height:39px">Email</div>
  <div class="field" style="left:256px;top:93px;width:579px;height:89px">Message</div>
  <div class="btn-send">SEND</div>
</form>

<div class="abs f-head" style="left:94px;top:4018px">Contact Us</div>
<div class="abs f-text" style="left:94px;top:4049px;line-height:30px">
  <div>&#9742;&nbsp; +61 7 3820 4416</div>
  <div>&#9647;&nbsp; +61 0455 208 913</div>
</div>
<div class="abs f-head" style="left:94px;top:4138px">Follow Us</div>
<div class="abs social" style="left:94px;top:4170px"><i></i><i></i><i></i><i></i><i></i><i></i></div>

<div class="abs f-head" style="left:386px;top:4018px">Philosophy</div>
<p class="abs f-text" style="left:386px;top:4049px;width:230px">As web developers, we understand that a powerful and functional web site is a vital component of modern day marketing for companies of today. This is why our web site development team work with all of our clients to ensure their web site design will deliver to their target market.</p>

<div class="abs f-head" style="left:725px;top:4018px">Quick Links</div>
<ul class="abs f-links" style="left:725px;top:4046px"><li>Home</li><li>Our Services</li><li>Our Clients</li><li>Contact</li></ul>

<div class="abs f-head" style="left:940px;top:4018px">Affiliates</div>
<div class="abs affiliate"><b></b>Novaline</div>
<div class="abs copyright">© 2019 <strong>Plumvista.net</strong>. All Right Reserved.</div>

</body>
</html>
```